Flyer Design Project

Paths of Yesteryear is a new collaborative of non-profit historical sites in the Greater Boston area. We're promoting the soft launch of our website by hosting open houses at each of the sites on September 21. We need a flyer to post up at each of the sites.

I have more print design needs to follow, and would really like to have a consistent look, so I intend to directly invite the winning designer to more projects.

Industry/Entity Type

Non-Profit

Requirements
Must have
• The flyer must be one page and be delivered as two files in Microsoft Publisher OR Microsoft Word. One file is for an 8 1/2 x 11 and one is as an 11 x 17 (same design, just scaled larger to fit the bigger paper).

It must have the Paths of Yesteryear Logo (attached), and this text (attached) and use black font.

Any color that is not black or white must be chosen from these colors-but don't feel you have to use all of them:

Paths of Yesteryear Website Colors

poppy red
c 0
m 93
y 87
k 0
web FF3333

nectarine
c 0
m 54
y 74
k 0
web FF9966

monaco blue

c 100
m 79
y 28
k 12
web 003366

tender shoots
c 30
m 0
y 89
k 0
web CCCC33

emerald
c 80
m 11
y 56
k 0
web 009999

african violet
c 28
m 44
y 0
k 0

web CC99CC

sunflower
c 10
m 33
y 99
k 0
web FF9933

lemon zest
c 4
m 13
y 77
k 0
web FFCC66

Nice to have
• Text and images with in the flyer should be large, simple and clear-as easy to see and read when the entire flyer is viewed on a mobile phone or from a distance as possible.

```html
<!DOCTYPE html>
<html lang="en">
<head>
<meta charset="utf-8">
<title>Paths of Yesteryear – Fall Open House</title>
<link rel="stylesheet" href="https://fonts.googleapis.com/css2?family=Didact+Gothic&family=Montserrat:wght@600&family=Oswald:wght@500;700&display=swap">
<style>
  :root {
    --page: #ececec;
    --lemon: #f6d35b;
    --violet: #b994c8;
    --violet-dark: #7b4e8c;
    --violet-mid: #9a6aae;
    --monaco: #1d4380;
    --shoots: #bcd84a;
    --nectarine: #f39a4a;
    --emerald: #12a08f;
    --poppy: #f03636;
    --ink: #111111;
    --white: #ffffff;
  }
  * { margin: 0; padding: 0; box-sizing: border-box; }
  html, body { width: 953px; height: 1200px; overflow: hidden; }
  body { background: var(--page); position: relative; font-family: "Didact Gothic", sans-serif; }

  .flyer {
    position: absolute; left: 66px; top: 74px;
    width: 809px; height: 1046px;
    background: var(--lemon); overflow: hidden;
    box-shadow: 0 6px 24px rgba(0,0,0,0.18);
  }
  .flyer-shapes { position: absolute; inset: 0; width: 100%; height: 100%; }

  .logo-symbol {
    position: absolute; left: 151px; top: 46px; width: 183px; height: 183px;
    background: linear-gradient(135deg, var(--violet) 0%, var(--nectarine) 45%, var(--shoots) 100%);
    opacity: 0.55; border-radius: 4px;
  }
  .wordmark {
    position: absolute; left: 347px; top: 50px;
    font-family: "Didact Gothic", sans-serif; font-size: 62px; line-height: 1.05;
    color: #0f3a73;
  }

  .event-date {
    position: absolute; left: 292px; top: 385px;
    transform: translate(-50%, -50%) rotate(44deg);
    font-family: "Oswald", sans-serif; font-weight: 700; font-size: 50px;
    color: var(--emerald); white-space: nowrap; letter-spacing: 0.5px;
  }

  .headline { position: absolute; left: 50px; top: 452px; color: var(--poppy); font-family: "Oswald", sans-serif; font-weight: 700; text-align: center; width: 200px; }
  .headline-season { display: block; font-size: 100px; line-height: 1; letter-spacing: 1px; }
  .headline-event { display: block; font-size: 36px; line-height: 1; font-weight: 500; margin-top: 2px; }

  .intro {
    position: absolute; left: 22px; top: 646px; width: 432px;
    font-size: 14.5px; line-height: 13.9px; color: var(--ink); word-spacing: -1px;
  }
  .web-button {
    position: absolute; left: 27px; top: 772px; width: 343px; height: 28px;
    background: var(--poppy); color: var(--white);
    font-family: "Montserrat", sans-serif; font-weight: 600; font-size: 14px;
    line-height: 28px; padding-left: 10px;
  }
  .web-button::after {
    content: ""; position: absolute; right: -10px; top: 4px;
    border-left: 12px solid #c92424; border-top: 10px solid transparent; border-bottom: 10px solid transparent;
  }

  .site-list {
    position: absolute; left: 22px; top: 830px;
    list-style: none; font-size: 14px; line-height: 13.4px; color: var(--ink); word-spacing: -1px;
  }

  .callout-art {
    position: absolute; left: 598px; top: 868px; width: 150px; height: 132px;
    background: var(--violet-dark); transform: rotate(-6deg);
  }
  .highlights {
    position: absolute; left: 488px; top: 742px; width: 210px; height: 164px;
    background: var(--violet-mid); transform: rotate(-7deg);
    display: flex; align-items: center; justify-content: center; text-align: center;
    font-family: "Oswald", sans-serif; font-weight: 700; font-size: 29px; line-height: 1.02;
    color: var(--white); text-shadow: 1px 1px 0 var(--violet-dark), -1px -1px 0 var(--violet-dark);
  }
</style>
</head>
<body>
  <div class="flyer">
    <svg class="flyer-shapes" viewBox="0 0 708 915" preserveAspectRatio="none" aria-hidden="true">
      <defs>
        <radialGradient id="steel" cx="0.5" cy="0.35" r="0.7">
          <stop offset="0" stop-color="#c9c9c9"/>
          <stop offset="1" stop-color="#5a5a5a"/>
        </radialGradient>
      </defs>
      <polygon points="0,0 220,0 0,210" fill="var(--violet)"/>
      <line x1="0" y1="210" x2="220" y2="0" stroke="var(--monaco)" stroke-width="3"/>
      <polygon points="218,0 708,0 708,718 97,120" fill="url(#steel)"/>
      <polygon points="222,242 267,183 708,650 708,718" fill="var(--shoots)"/>
      <line x1="97" y1="120" x2="708" y2="720" stroke="var(--nectarine)" stroke-width="4"/>
    </svg>

    <div class="logo-symbol" role="img" aria-label="Paths of Yesteryear logo symbol"></div>
    <div class="wordmark">Paths of<br>Yesteryear</div>

    <div class="event-date">Saturday, September 21</div>

    <h1 class="headline">
      <span class="headline-season">FALL</span>
      <span class="headline-event">OPEN HOUSE</span>
    </h1>

    <p class="intro">Columbus. Pilgrims. Revolution. Civil War. Industrialization. You know the history. But do you know the stories? Have you found how YOU are connected to the places and lives of the people who’ve shaped our world, our country, our state, and your life today? Find out by exploring some of Massachusetts’ treasured historical gems—you’ll be sur­prised by the wealth you discover.<br>For hours, directions, and discount/prize passes</p>

    <div class="web-button">learn more at www.pathsofyesteryear.org</div>

    <ul class="site-list">
      <li>Briar Hill at Lowden Estate</li>
      <li>"Church of the Founders" Old North Parish (Unitarian) of Hartwell</li>
      <li>Ashcombe Memorial Library</li>
      <li>Elena Marsh Dance Theatre's Home at Old Fenwick Baptist Church</li>
      <li>Thayer's Boat Shop and Museum</li>
      <li>Mount Linden Cemetery</li>
      <li>Museum of Harbor Heritage: Riverside Campus</li>
      <li>Museum of Harbor Heritage: Island Campus</li>
      <li>Memorial to the First Settlers</li>
      <li>Old Anchor Meeting House</li>
      <li>The Seabright Park Carousel</li>
      <li>Silas Whitcomb House</li>
      <li>The Harmon Hall, Brookfield's Center for Folk Culture</li>
    </ul>

    <div class="callout-art" role="img" aria-label="Folded paper ribbon illustration in violet tones"></div>
    <div class="highlights">Special Tours,<br>Games, Prizes,<br>and Children’s<br>Activities!</div>
  </div>
</body>
</html>
```